STATIONERY and Brand ID for KelvaBank

We need a family of identical Brand guide
Call Card
Envelope
Letterhead
Poster
Brochure

It needs to have an international Fee/

The ARCHITECTURE/STRUCTURE must show the highest level of creativity

1. Call card could be two sided
2. cal card can have a a flap
3. Call card can have a curved edge

Target Market(s)

Business and bank clients

Industry/Entity Type

Bank

Requirements
Must have
• the logo atatched
• the colour scheme must be used
• There must be a common look and feel and they must have the same DNA

```html
<!DOCTYPE html>
<html lang="en">
<head>
<meta charset="utf-8">
<title>KelvaBank Envelope</title>
<link rel="stylesheet" href="https://fonts.googleapis.com/css2?family=Arimo:wght@400;700&display=swap">
<style>
  :root {
    --brand-green: #0b9a3e;
    --ink: #1c1c1c;
    --paper: #ffffff;
  }
  * { margin: 0; padding: 0; box-sizing: border-box; }
  html, body {
    width: 1200px;
    height: 544px;
    overflow: hidden;
    background: var(--paper);
  }
  .envelope {
    position: relative;
    width: 1200px;
    height: 544px;
    background: var(--paper);
    font-family: "Arimo", Arial, sans-serif;
    color: var(--ink);
  }
  .brand-name {
    position: absolute;
    left: 72px;
    top: 66px;
    font-weight: 700;
    font-size: 64px;
    line-height: 1;
    letter-spacing: -1px;
    color: var(--brand-green);
  }
  .return-address {
    position: absolute;
    left: 73px;
    top: 402px;
    font-style: normal;
    font-size: 12.5px;
    line-height: 17px;
  }
  .contact-list {
    position: absolute;
    left: 73px;
    top: 442px;
    list-style: none;
    font-size: 12.5px;
  }
  .contact-list li {
    display: flex;
    align-items: center;
    height: 19px;
  }
  .contact-list svg {
    width: 15px;
    height: 15px;
    margin-right: 11px;
    flex: none;
  }
</style>
</head>
<body>
  <main class="envelope">
    <header>
      <span class="brand-name">KelvaBank</span>
    </header>

    <address class="return-address">
      4120 Harbor Crest Drive<br>
      Bayview, CA&nbsp;&nbsp; 92110
    </address>

    <ul class="contact-list">
      <li>
        <svg viewBox="0 0 16 16" aria-hidden="true">
          <circle cx="8" cy="8" r="8" fill="var(--brand-green)"/>
          <path d="M5.2 4.2c.5-.4 1-.3 1.2.2l.6 1.4c.2.4 0 .8-.3 1l-.5.4c.4 1 1.2 1.9 2.2 2.4l.5-.5c.3-.3.7-.4 1-.2l1.4.7c.4.2.5.8.1 1.2-.6.7-1.4 1-2.2.7C6.8 10.8 5 8.9 4.5 6.6c-.2-.9.1-1.8.7-2.4z" fill="#fff"/>
        </svg>
        555 240 7718
      </li>
      <li>
        <svg viewBox="0 0 16 16" aria-hidden="true">
          <rect x="0.5" y="3" width="15" height="10" fill="var(--brand-green)"/>
          <path d="M0.8 3.4 8 9l7.2-5.6M0.8 12.6l5.2-4.6M15.2 12.6 10 8" stroke="#fff" stroke-width="1" fill="none"/>
        </svg>
        Jordan.Hale@kelvabank.example
      </li>
      <li>
        <svg viewBox="0 0 16 16" aria-hidden="true">
          <circle cx="8" cy="8" r="7.5" fill="var(--brand-green)"/>
          <path d="M3.5 5c1 .2 1.8 1 1.6 2-.2.8.8 1.2.8 2.2 0 .8-.6 1.4-.4 2.6M9 2c-.4 1 .4 1.6 1.4 1.8 1 .2 1 1.2.4 1.8-.6.6-.2 1.6.8 1.6h1.8M9.5 14c0-1 .6-1.6 1.4-2 .8-.4.8-1.4 2-1.4" stroke="#fff" stroke-width="1.1" fill="none" stroke-linecap="round"/>
        </svg>
        www.kelvabank.example
      </li>
    </ul>
  </main>
</body>
</html>
```